Enterprise Application UI beautification

We have an enterprise application that is being redesigned. A screenshot from the new UX/UI is provided. The current UI design is OK but we would like it to look better. The key goals of the UI are to look like a premium product (think luxury brand) and for it to be visually very appealing/attractive. When people see the UI we want them to have a significant, positive reaction. They should "ooh" and "ahh". This is a product sold to large enterprises, not consumers. The current UI is a little plain. The colors we want to use are blue, yellow, black, white and gray. We probably don't want different colors but feel free to use any variations within or close to that color scheme that you see fit. Also feel free to modify the spacing, icons, widgets, tables, fonts, etc.

Target Market(s)

Large enterprise customers (Summit 300).

Number of Pages Required

1 page

Font styles to use
Sans Serif

Colors
3277b5

Requirements
Must have
• A premium feel.

```html
<!DOCTYPE html>
<html lang="en">
<head>
<meta charset="utf-8">
<title>Data Sources – CloudLedger Sandbox</title>
<link href="https://fonts.googleapis.com/css2?family=Orbitron:wght@500;600;700&family=Open+Sans:wght@400;600&display=swap" rel="stylesheet">
<style>
:root{
  --blue:#3277b5;
  --blue-deep:#1d4f80;
  --navy:#0f1f33;
  --navy-2:#182c45;
  --gold:#e9b949;
  --gold-soft:#f6e3ae;
  --ink:#14202e;
  --ink-soft:#3d4a5a;
  --muted:#7f8b99;
  --faint:#d3dbe4;
  --panel:#eaf0f6;
  --line:#d6dee7;
  --paper:#ffffff;
  --page:#f7f9fb;
}
*{box-sizing:border-box;margin:0;padding:0}
html,body{width:1200px;height:656px;overflow:hidden;background:var(--page)}
body{position:relative;font-family:'Orbitron',sans-serif;color:var(--ink)}
.abs{position:absolute}

.rail{left:0;top:0;width:52px;height:656px;background:linear-gradient(180deg,var(--navy),var(--navy-2))}
.rail-item{position:absolute;left:0;width:52px;display:flex;align-items:center;justify-content:center;border-top:1px solid rgba(255,255,255,.08)}
.rail-item.active{background:linear-gradient(90deg,var(--blue-deep),var(--blue));box-shadow:inset 3px 0 0 var(--gold)}
.menu-tab{left:52px;top:225px;width:26px;height:206px;background:linear-gradient(90deg,var(--blue-deep),var(--blue));border-radius:0 14px 14px 0;box-shadow:3px 2px 8px rgba(15,31,51,.35);display:flex;align-items:center;justify-content:center}
.menu-tab span{writing-mode:vertical-rl;font-size:10px;font-weight:700;letter-spacing:3px;color:var(--gold)}

.sidebar{left:52px;top:0;width:278px;height:656px;background:var(--paper)}
.brand{left:77px;top:32px;display:flex;align-items:center;gap:8px;font-size:17px;font-weight:700;color:var(--navy);letter-spacing:1px}
.brand i{width:14px;height:14px;border-radius:50%;background:var(--gold);display:block}
.h-section{font-size:15px;font-weight:700;letter-spacing:.8px;color:var(--navy)}
.add-btn{width:28px;height:28px;background:linear-gradient(135deg,var(--blue),var(--blue-deep));border-radius:4px;display:flex;align-items:center;justify-content:center;box-shadow:0 2px 5px rgba(50,119,181,.35)}
.search{left:77px;top:136px;width:230px;height:31px;border-radius:16px;background:var(--panel);border:1px solid var(--line);display:flex;align-items:center;justify-content:space-between;padding:0 3px 0 12px;font-family:'Open Sans',sans-serif;font-size:13px;color:var(--muted)}
.search b{width:34px;height:23px;background:var(--navy);display:flex;align-items:center;justify-content:center;border-radius:12px}
.source{position:absolute;left:82px;width:232px}
.source .name{font-size:10.5px;font-weight:600;letter-spacing:.5px;color:var(--ink);white-space:nowrap}
.source .name em{font-style:normal;color:var(--blue)}
.source .kind{font-size:6.5px;letter-spacing:.6px;color:var(--muted);margin-top:4px}
.source.current .name{color:var(--blue-deep)}
.source.current::before{content:"";position:absolute;left:-8px;top:-2px;width:3px;height:24px;background:var(--gold);border-radius:2px}
.scroll-left{left:314px;top:230px;width:5px;height:287px;border-radius:3px;background:var(--faint)}
.scroll-left i{display:block;width:5px;height:90px;border-radius:3px;background:var(--blue)}

.divider{left:330px;top:0;width:22px;height:656px;background:linear-gradient(180deg,var(--navy),var(--blue-deep) 50%,var(--navy))}
.divider-rule{left:340px;top:0;width:2px;height:656px;background:var(--gold)}
.band-h{left:778px;top:53px;width:287px;height:5px;background:linear-gradient(90deg,var(--gold),var(--gold-soft));border-radius:3px}

.title{left:368px;top:45px;font-size:16.5px;font-weight:700;letter-spacing:1px;color:var(--navy)}
.tool{position:absolute;top:40px;width:29px;text-align:center}
.tool .box{width:29px;height:29px;background:var(--paper);border:1px solid var(--line);border-radius:5px;display:flex;align-items:center;justify-content:center;box-shadow:0 2px 4px rgba(15,31,51,.08)}
.tool.danger .box{border-color:#e8c8c8}
.tool .lbl{font-family:'Open Sans',sans-serif;font-size:10px;color:var(--ink-soft);margin-top:4px;margin-left:-10px;width:49px}
.user{left:1073px;font-family:'Open Sans',sans-serif;font-size:11px;display:flex;align-items:center;gap:8px;color:var(--ink)}

.info{left:367px;top:94px;width:806px;height:152px;display:grid;grid-template-columns:repeat(4,1fr);border:1px solid var(--line);border-radius:6px;overflow:hidden;background:var(--paper);box-shadow:0 4px 14px rgba(15,31,51,.06)}
.info .col{padding:10px 9px 0 9px;font-size:9.5px;letter-spacing:.6px;line-height:27.7px;white-space:nowrap}
.info .col.key{background:var(--panel);color:var(--ink-soft);font-weight:500}
.info .col.val{color:var(--navy);font-weight:600}
.info .col+.col{border-left:1px solid var(--line)}

.obj-row{position:absolute;left:367px;font-size:11px;font-weight:600;letter-spacing:.6px;display:flex;align-items:center;color:var(--navy)}
.grip{font-size:8px;color:var(--blue);margin-right:6px;letter-spacing:-1px}
.fields{left:525px;top:304px;font-size:10.5px;font-weight:600;display:flex;align-items:center;gap:5px;color:var(--navy)}
.fields .add-btn{width:18px;height:18px;border-radius:3px}

table{position:absolute;left:367px;top:335px;width:806px;border-collapse:separate;border-spacing:0;font-size:9.5px;letter-spacing:.5px;background:var(--paper);border:1px solid var(--line);border-radius:6px;overflow:hidden;table-layout:fixed}
th{background:linear-gradient(180deg,var(--navy-2),var(--navy));color:#fff;height:40px;text-align:left;font-weight:600;padding:0 7px;border-bottom:2px solid var(--gold);font-size:9px;white-space:nowrap}
th.c{text-align:center}
td{height:27.6px;padding:0 7px;vertical-align:middle;color:var(--ink);white-space:nowrap}
td+td{border-left:1px solid var(--line)}
tbody tr:first-child td{height:31px;padding-top:3px}
tbody tr:last-child td{height:28px}
.pk{width:18px;height:18px;background:var(--faint);border-radius:3px;display:flex;align-items:center;justify-content:center;margin:0 auto}
.pk.on{background:var(--gold)}
.rules{display:flex;gap:7px;align-items:center}
.rules svg{width:14px;height:14px}
.dim{opacity:.28}
.acts{display:flex;gap:14px;justify-content:center}
.mini{width:18px;height:18px;background:var(--panel);border-radius:3px;display:flex;align-items:center;justify-content:center}
.sens{display:flex;gap:14px;justify-content:center;align-items:center}
.obj{position:absolute;left:367px;width:806px;height:38px;border-bottom:1px solid var(--line)}
.obj .obj-row{position:absolute;left:3px;top:11px}
.obj .mini{position:absolute;left:163px;top:9px}
.scroll-right{left:1184px;top:304px;width:5px;height:220px;border-radius:3px;background:var(--blue)}
</style>
</head>
<body>
<svg width="0" height="0" style="position:absolute">
  <defs>
    <symbol id="i-x" viewBox="0 0 10 10"><path d="M2 2L8 8M8 2L2 8" stroke="#14202e" stroke-width="2" stroke-linecap="round"/></symbol>
    <symbol id="i-plus" viewBox="0 0 10 10"><path d="M5 1v8M1 5h8" stroke="#fff" stroke-width="2.4" stroke-linecap="round"/></symbol>
    <symbol id="i-edit" viewBox="0 0 16 16"><rect x="2" y="3" width="10" height="11" rx="1" fill="none" stroke="#1d4f80" stroke-width="1.4"/><path d="M7 10l1-3 6-6 2 2-6 6z" fill="#3277b5"/></symbol>
    <symbol id="i-link" viewBox="0 0 14 14"><path d="M3 5h8a2 2 0 010 4H3a2 2 0 010-4" fill="none" stroke="#1d4f80" stroke-width="2"/></symbol>
    <symbol id="i-search" viewBox="0 0 14 14"><circle cx="6" cy="6" r="4" fill="none" stroke="#1d4f80" stroke-width="1.5"/><path d="M9 9l4 4" stroke="#1d4f80" stroke-width="1.8"/></symbol>
    <symbol id="i-search-w" viewBox="0 0 14 14"><circle cx="6" cy="6" r="4" fill="none" stroke="#fff" stroke-width="1.5"/><path d="M9 9l4 4" stroke="#e9b949" stroke-width="1.8"/></symbol>
    <symbol id="i-sq" viewBox="0 0 14 14"><rect x="2" y="2" width="10" height="10" fill="none" stroke="#1d4f80" stroke-width="1.3"/><rect x="2" y="7" width="5" height="5" fill="none" stroke="#1d4f80" stroke-width="1.3"/></symbol>
    <symbol id="i-tree" viewBox="0 0 14 14"><g fill="none" stroke="#1d4f80" stroke-width="1"><rect x="1" y="1" width="4" height="4"/><rect x="8" y="1" width="4" height="4"/><rect x="5" y="9" width="4" height="4"/><path d="M3 5v2h7V5M7 7v2"/></g></symbol>
    <symbol id="i-target" viewBox="0 0 14 14"><circle cx="7" cy="7" r="4.5" fill="none" stroke="#1d4f80" stroke-width="1.2"/><path d="M7 0v4M7 10v4M0 7h4M10 7h4" stroke="#1d4f80" stroke-width="1.2"/></symbol>
    <symbol id="i-arrow" viewBox="0 0 14 14"><path d="M5 4l4 3-4 3z" fill="#1d4f80"/></symbol>
    <symbol id="i-check" viewBox="0 0 14 14"><path d="M2 7l3.5 4L12 3" fill="none" stroke="#0f1f33" stroke-width="2.4"/></symbol>
  </defs>
</svg>

<nav class="abs rail" aria-label="Main navigation">
  <div class="rail-item" style="top:130px;height:65px"><svg width="24" height="22" viewBox="0 0 24 22"><g fill="#dfe8f2"><circle cx="5" cy="5" r="2.5"/><circle cx="12" cy="4" r="3"/><circle cx="19" cy="5" r="2.5"/><rect x="2" y="9" width="6" height="9" rx="2"/><rect x="8.5" y="8" width="7" height="13" rx="2"/><rect x="16" y="9" width="6" height="9" rx="2"/></g></svg></div>
  <div class="rail-item" style="top:195px;height:68px"><svg width="24" height="16" viewBox="0 0 24 16"><path d="M6 15a5 5 0 010-10 7 7 0 0113 2 4 4 0 010 8z" fill="#dfe8f2"/><path d="M12 6l-3 4h2v3h2v-3h2z" fill="#0f1f33"/></svg></div>
  <div class="rail-item active" style="top:263px;height:66px"><svg width="30" height="26" viewBox="0 0 30 26"><rect x="5" y="2" width="20" height="8" fill="none" stroke="#fff" stroke-width="2"/><rect x="1" y="10" width="28" height="14" rx="2" fill="#fff"/><rect x="12" y="15" width="6" height="2" fill="#e9b949"/></svg></div>
  <div class="rail-item" style="top:329px;height:67px"><svg width="18" height="24" viewBox="0 0 18 24"><rect x="1" y="3" width="16" height="20" rx="1" fill="#dfe8f2"/><rect x="5" y="1" width="8" height="4" fill="#dfe8f2" stroke="#0f1f33"/><path d="M4 10h2M8 10h6M4 14h2M8 14h6M4 18h2M8 18h6" stroke="#0f1f33" stroke-width="1.5"/></svg></div>
  <div class="rail-item" style="top:396px;height:69px"><svg width="20" height="22" viewBox="0 0 20 22"><rect x="1" y="4" width="18" height="17" rx="1" fill="#dfe8f2"/><rect x="1" y="4" width="18" height="4" fill="#e9b949"/><path d="M5 1v5M15 1v5" stroke="#dfe8f2" stroke-width="2"/><g fill="#0f1f33"><rect x="4" y="11" width="3" height="3"/><rect x="9" y="11" width="3" height="3"/><rect x="14" y="11" width="3" height="3"/><rect x="4" y="16" width="3" height="3"/><rect x="9" y="16" width="3" height="3"/></g></svg></div>
  <div class="rail-item" style="top:465px;height:52px;border-bottom:1px solid rgba(255,255,255,.08)"><svg width="22" height="22" viewBox="0 0 22 22"><path d="M18 9A8 8 0 004 7M4 13a8 8 0 0014 2" fill="none" stroke="#dfe8f2" stroke-width="2.6"/><path d="M1 4l4 5 4-4zM21 18l-4-5-4 4z" fill="#dfe8f2"/></svg></div>
</nav>

<aside class="abs sidebar"></aside>
<div class="abs menu-tab"><span>MENU</span></div>

<div class="abs brand"><i></i>Axion</div>

<div class="abs h-section" style="left:77px;top:101px">Data Sources</div>
<div class="abs add-btn" style="left:272px;top:94px"><svg width="13" height="13"><use href="#i-plus"/></svg></div>
<div class="abs search">Search<b><svg width="14" height="14"><use href="#i-search-w"/></svg></b></div>

<div class="source current" style="top:192px"><div class="name">CloudLedger Sandbox</div><div class="kind">cloudledger.io</div></div>
<div class="source" style="top:251px"><div class="name">PostBase Test - 1 "<em>Admin</em>"</div><div class="kind">PostBase SQL</div></div>
<div class="source" style="top:310px"><div class="name">PostBase Test - 2 "<em>Admin</em>"</div><div class="kind">PostBase SQL</div></div>
<div class="source" style="top:369px"><div class="name">Sadga</div><div class="kind">cloudledger.io</div></div>
<div class="source" style="top:428px"><div class="name">CloudLedger Test-1 "Mastered ec"</div><div class="kind">PostBase SQL</div></div>
<div class="source" style="top:487px"><div class="name">CLDG - Field Entry Test</div><div class="kind">cloudledger.io</div></div>
<div class="source" style="top:546px"><div class="name">CLDG <em>44</em> - Field Entry Test</div><div class="kind">cloudledger.io</div></div>
<div class="source" style="top:605px"><div class="name">CLDG <em>66</em> - Field Entry Test</div><div class="kind">cloudledger.io</div></div>
<div class="abs scroll-left"><i></i></div>

<div class="abs divider" role="img" aria-label="Decorative key-pattern divider band"></div>
<div class="abs divider-rule"></div>

<div class="abs title">CloudLedger - Sandbox</div>
<div class="tool" style="left:646px"><div class="box"><svg width="17" height="17"><use href="#i-edit"/></svg></div><div class="lbl">Edit</div></div>
<div class="tool" style="left:693px"><div class="box"><svg width="16" height="16"><use href="#i-tree"/></svg></div><div class="lbl">Clone</div></div>
<div class="tool danger" style="left:740px"><div class="box"><svg width="13" height="13"><use href="#i-x"/></svg></div><div class="lbl">Delete</div></div>
<div class="abs band-h" role="img" aria-label="Decorative key-pattern ornament band"></div>
<div class="abs user" style="top:32px"><svg width="19" height="19" viewBox="0 0 20 20"><circle cx="10" cy="10" r="6" fill="none" stroke="#1d4f80" stroke-width="4" stroke-dasharray="3 2"/><circle cx="10" cy="10" r="4" fill="#1d4f80"/><circle cx="10" cy="10" r="1.6" fill="#e9b949"/></svg>Fran Fixwell</div>
<div class="abs user" style="top:61px"><svg width="19" height="19" viewBox="0 0 20 20"><circle cx="10" cy="10" r="8.5" fill="none" stroke="#1d4f80" stroke-width="1.3"/><circle cx="10" cy="10" r="6" fill="none" stroke="#3277b5"/><path d="M10 10l3-4" stroke="#e9b949" stroke-width="1.6"/></svg>Test Conection</div>

<section class="abs info">
  <div class="col key">Data Source Name<br>Data Source Type<br>Status<br>Created By<br>Last Updated By</div>
  <div class="col val">CloudLedger-Sandbox<br>Application<br>Active<br>northwind.test<br>northwind.test</div>
  <div class="col key">User Name<br>Security Token<br>Enviroment Type<br>Connected App</div>
  <div class="col val">admin@devhub.net<br>Data Source Type<br>tadkaji4234ifndkn3<br>No</div>
</section>

<div class="abs h-section" style="left:368px;top:267px">Data Objects</div>
<div class="abs add-btn" style="left:524px;top:258px"><svg width="13" height="13"><use href="#i-plus"/></svg></div>

<div class="obj-row" style="top:306px"><span class="grip">∴∴</span>Account</div>
<div class="abs fields">Fields <span class="add-btn"><svg width="9" height="9"><use href="#i-plus"/></svg></span></div>

<table>
  <colgroup><col style="width:193px"><col style="width:194px"><col style="width:86px"><col style="width:123px"><col style="width:122px"><col style="width:88px"></colgroup>
  <thead><tr><th>Field Name</th><th>Data Type</th><th class="c" style="padding:0 2px;font-size:8.5px">Primary Key</th><th>Rule Types</th><th class="c">Sensitive Data</th><th class="c">Actions</th></tr></thead>
  <tbody>
    <tr><td>Account Descreption</td><td>Common. Text</td><td><span class="pk on"><svg width="13" height="13"><use href="#i-check"/></svg></span></td>
      <td><div class="rules"><svg><use href="#i-link"/></svg><svg class="dim"><use href="#i-search"/></svg><svg><use href="#i-sq"/></svg><svg class="dim"><use href="#i-tree"/></svg><svg class="dim"><use href="#i-target"/></svg><svg class="dim"><use href="#i-arrow"/></svg></div></td>
      <td><div class="sens"><svg width="12" height="16" viewBox="0 0 12 16"><rect x="1" y="3" width="10" height="12" fill="#3277b5"/><rect x="4" y="1" width="4" height="3" fill="#3277b5"/><path d="M6 6v6M3 9h6" stroke="#fff" stroke-width="1.6"/></svg><svg width="16" height="12" viewBox="0 0 16 12"><rect x="0" y="1" width="16" height="4" fill="#3277b5"/><rect x="0" y="7" width="12" height="4" fill="#e9b949"/></svg><svg width="12" height="16" viewBox="0 0 12 16"><circle cx="6" cy="3.5" r="3" fill="#3277b5"/><rect x="1" y="8" width="10" height="8" rx="2" fill="#3277b5"/></svg></div></td>
      <td><div class="acts"><span class="mini"><svg width="12" height="12"><use href="#i-edit"/></svg></span><span class="mini"><svg width="9" height="9"><use href="#i-x"/></svg></span></div></td></tr>
    <tr><td>Account Fax</td><td>Address. Address line 3</td><td><span class="pk"></span></td>
      <td><div class="rules"><svg class="dim"><use href="#i-link"/></svg><svg class="dim"><use href="#i-search"/></svg><svg><use href="#i-sq"/></svg><svg class="dim"><use href="#i-tree"/></svg><svg class="dim"><use href="#i-target"/></svg><svg class="dim"><use href="#i-arrow"/></svg></div></td><td></td>
      <td><div class="acts"><span class="mini"><svg width="12" height="12"><use href="#i-edit"/></svg></span><span class="mini"><svg width="9" height="9"><use href="#i-x"/></svg></span></div></td></tr>
    <tr><td>Account ID</td><td>Status</td><td><span class="pk"></span></td>
      <td><div class="rules"><svg><use href="#i-link"/></svg><svg><use href="#i-search"/></svg><svg class="dim"><use href="#i-sq"/></svg><svg class="dim"><use href="#i-tree"/></svg><svg class="dim"><use href="#i-target"/></svg><svg class="dim"><use href="#i-arrow"/></svg></div></td><td></td>
      <td><div class="acts"><span class="mini"><svg width="12" height="12"><use href="#i-edit"/></svg></span><span class="mini"><svg width="9" height="9"><use href="#i-x"/></svg></span></div></td></tr>
    <tr><td>Account Name</td><td>Created By</td><td><span class="pk"></span></td>
      <td><div class="rules"><svg class="dim"><use href="#i-link"/></svg><svg class="dim"><use href="#i-search"/></svg><svg><use href="#i-sq"/></svg><svg class="dim"><use href="#i-tree"/></svg><svg class="dim"><use href="#i-target"/></svg><svg class="dim"><use href="#i-arrow"/></svg></div></td><td></td>
      <td><div class="acts"><span class="mini"><svg width="12" height="12"><use href="#i-edit"/></svg></span><span class="mini"><svg width="9" height="9"><use href="#i-x"/></svg></span></div></td></tr>
  </tbody>
</table>

<div class="obj" style="top:493px"><div class="obj-row"><span class="grip">⁘⁘</span>Asset</div><span class="mini"><svg width="9" height="9"><use href="#i-x"/></svg></span></div>
<div class="obj" style="top:531px"><div class="obj-row"><span class="grip">⁘⁘</span>Asset Relationship</div><span class="mini"><svg width="9" height="9"><use href="#i-x"/></svg></span></div>
<div class="obj" style="top:569px"><div class="obj-row"><span class="grip">⁘⁘</span>Asset Token Event</div><span class="mini"><svg width="9" height="9"><use href="#i-x"/></svg></span></div>
<div class="obj" style="top:606px"><div class="obj-row"><span class="grip">⁘⁘</span>Case</div><span class="mini"><svg width="9" height="9"><use href="#i-x"/></svg></span></div>

<div class="abs scroll-right"></div>
</body>
</html>
```